Business card - house cleaning company

We want friendly high end business card highlighting our services . NO LOGOs on back of card please.. no vertical cards NO DOUBLE BROOMS

2 owners of the company: Corinne Hale & Dean Oakley

Included phone number: (555)318-2207

Email: brightnookclean@example.net

Website: www.brightnookclean.example

Bonded & Insured

Cedar Vale, NV 80999

Slogan maybe: Helping your home shine for a cleaner tomorrow

We want elegant high end card for house cleaning service. Maybe 2 sided if needed. Can it have bullet points of some services we offer

Residential Home Cleaning
Vacation Rental Cleaning
Commercial Cleaning
Carpet Cleaning
Window Cleaning
Property Management
Property Inspections
Property Maintenance
Trash Removal
Concierge Services

Highlight service on back of card. If we can do a one sided card with all this that’s great as well. Not cartoony.

Our logo attached and a design somone I had Harlan but they put very little time in. Not Unique enough. If you can do a custom design with a feminine touch that be great.

You will be eliminated for not reading the brief. NO DOUBLE LOGOS NO DOUBLE BROOMS. PLEASE BE CREATIVE. IF POST SAME LOGO WITH SMAL CHANGES RHEY WILL BE ELIMINATED. BE CREATIVE.
Updates

Thank you everyone for your designs. please only use the logo 1 time. and would love to see some that dont look all the same. We appreciate your time.

Target Market(s)

Residential and vacation rental home cleaning maid service

Industry/Entity Type

House cleaning maid services

Contact Information for Business Card

For business card use logo. black and green one provided. others for example. I wil try find some example.. We want friendly high end look. 2 owners of the company: Corinne Hale & Dean Oakley Included phone number: (555)318-2207 Email: brightnookclean@example.net Website: www.brightnookclean.example Bonded & Insured Cedar Vale, NV Slogan maybe: Helping your home shine for a cleaner tomorrow or Quality Service Guaranteed We want elegant high end card for house cleaning service. Maybe 2 sided if needed. Can it have bullet points of some services we offer Residential Home Cleaning Vacation Rental Cleaning Commercial Cleaning Carpet Cleaning Window Cleaning Property Management Property Inspections Property Maintenance Trash Removal Concierge Services

Requirements
Must have
• For business card use logo . Creativity. black and green one provided. We want friendly high end look. 2 owners of the company: Corinne Hale & Dean Oakley Included phone number: (555)318-2207 Email: brightnookclean@example.net Website: www.brightnookclean.example Licensed Bonded & Insured Cedar Vale, NV Slogan maybe: Helping your home shine for a cleaner tomorrow or Quality Service Guaranteed We want elegant high end card for house cleaning service. Maybe 2 sided if needed. Can it have bullet points of some services we offer Residential Home Cleaning Vacation Rental Cleaning Commercial Cleaning Carpet Cleaning Window Cleaning Property Management Property Inspections Property Maintenance Trash Removal Concierge Services .. creatitivty a plus. whimsical. we like stars..
Nice to have
• we want much better than the example of biz card provided as example. logo has colors that are in our website palette as well. We are open to ideas for the business card design. Will pay tip to best work. PLEASE USE COMPLIMENTING COLORS. . WE LIKE BLACK AND WHITE, stars
Should not have
• NO DOUBLE LOGOS. READ READ. READ. YOU WILL BE ELIMINATED no double logos or double brooms same side of card. I want didfrent examples. please don't make all your submission look the same

```html
<!DOCTYPE html>
<html lang="en">
<head>
<meta charset="utf-8">
<title>Bright Nook Cleaning Services – Business Card</title>
<link rel="stylesheet" href="https://fonts.googleapis.com/css2?family=Arimo:wght@400;700&display=swap">
<style>
  :root {
    --page: #e9ebee;
    --brand-blue: #2d6690;
    --brand-blue-dark: #245677;
    --brand-green: #6b9a3c;
    --rule-gray: #9a9a9a;
    --white: #ffffff;
    --ink-blue: #2a5f88;
  }
  * { box-sizing: border-box; margin: 0; padding: 0; }
  html, body {
    width: 1200px; height: 1015px; overflow: hidden;
    background: var(--page);
    font-family: "Arimo", Arial, sans-serif;
  }
  .card {
    position: absolute;
    width: 700px; height: 400px;
    box-shadow: 0 10px 28px rgba(0,0,0,.22);
    overflow: hidden;
  }

  /* Back side: services */
  .card-back {
    left: 60px; top: 70px;
    background: var(--brand-blue);
    color: var(--white);
  }
  .card-back .pattern-area {
    position: absolute; inset: 0;
    background: linear-gradient(135deg, var(--brand-blue) 0%, var(--brand-blue-dark) 100%);
  }
  .services {
    position: absolute; top: 150px; left: 70px; right: 40px;
    display: flex; gap: 40px;
  }
  .services ul { list-style: none; }
  .services li {
    font-size: 17px; letter-spacing: .4px; line-height: 31px;
    text-transform: uppercase; white-space: nowrap;
  }
  .services li::before {
    content: ""; display: inline-block;
    width: 8px; height: 8px; border-radius: 50%;
    background: var(--white); margin-right: 9px; vertical-align: 2px;
  }

  /* Front side: contact */
  .card-front {
    left: 440px; top: 545px;
    background: var(--white);
  }
  .brand {
    position: absolute; top: 52px; right: 44px;
    display: flex; align-items: center; gap: 12px;
  }
  .brand-dot { width: 22px; height: 22px; border-radius: 50%; background: var(--brand-green); }
  .brand-name {
    font-size: 27px; font-weight: 700; color: var(--brand-blue);
  }
  .brand-rule {
    position: absolute; top: 112px; right: 30px; width: 290px;
    border-top: 1px solid var(--rule-gray);
  }
  .owners {
    position: absolute; top: 150px; left: 50px;
    font-size: 27px; font-weight: 700; color: var(--brand-green);
    text-transform: uppercase; letter-spacing: .3px;
  }
  .owners-rule {
    position: absolute; top: 192px; left: 50px; width: 590px;
    border-top: 1px solid var(--rule-gray);
  }
  .contact {
    position: absolute; top: 206px; left: 56px;
    list-style: none;
  }
  .contact li {
    display: flex; align-items: center; gap: 10px;
    font-size: 17px; line-height: 25px; color: var(--ink-blue);
  }
  .contact svg { width: 17px; height: 17px; fill: var(--brand-green); flex: none; }
  .credential {
    position: absolute; top: 272px; right: 44px;
    font-size: 17px; color: var(--brand-green);
    text-transform: uppercase; letter-spacing: .4px;
  }
  .slogan-band {
    position: absolute; left: 0; right: 0; bottom: 0; height: 56px;
    background: var(--brand-blue);
    display: flex; align-items: center; justify-content: center;
  }
  .slogan {
    color: var(--white); font-size: 18px; letter-spacing: .8px;
    text-transform: uppercase;
  }
</style>
</head>
<body>

<section class="card card-back" aria-label="Back of card: services">
  <div class="pattern-area" role="img" aria-label="Faint repeating pattern of brooms and rooftops in tone-on-tone blue"></div>
  <div class="services">
    <ul>
      <li>Residential Home Cleaning</li>
      <li>Vacation Rental Cleaning</li>
      <li>Commercial Cleaning</li>
      <li>Carpet Cleaning</li>
      <li>Window Cleaning</li>
    </ul>
    <ul>
      <li>Property Management</li>
      <li>Property Inspections</li>
      <li>Property Maintenance</li>
      <li>Trash Removal</li>
      <li>Concierge Services</li>
    </ul>
  </div>
</section>

<section class="card card-front" aria-label="Front of card: contact details">
  <div class="brand">
    <span class="brand-dot"></span>
    <span class="brand-name">Bright Nook Cleaning Services</span>
  </div>
  <div class="brand-rule"></div>

  <h1 class="owners">Corinne Hale &amp; Dean Oakley</h1>
  <div class="owners-rule"></div>

  <ul class="contact">
    <li>
      <svg viewBox="0 0 24 24" aria-hidden="true"><path d="M6.6 10.8a15.1 15.1 0 0 0 6.6 6.6l2.2-2.2a1 1 0 0 1 1-.25 11.4 11.4 0 0 0 3.6.57 1 1 0 0 1 1 1V20a1 1 0 0 1-1 1A17 17 0 0 1 3 4a1 1 0 0 1 1-1h3.5a1 1 0 0 1 1 1c0 1.25.2 2.45.57 3.57a1 1 0 0 1-.25 1z"/></svg>
      (555)318-2207
    </li>
    <li>
      <svg viewBox="0 0 24 24" aria-hidden="true"><path d="M2 5h20v14H2zm2 2v.5l8 5 8-5V7l-8 5z"/></svg>
      brightnookclean@example.net
    </li>
    <li>
      <svg viewBox="0 0 24 24" aria-hidden="true"><path d="M12 2a10 10 0 1 0 0 20 10 10 0 0 0 0-20zm7.9 9h-3.4a15 15 0 0 0-1.3-6A8 8 0 0 1 19.9 11zM12 4.1c.9 1.3 2 3.7 2.4 6.9H9.6C10 7.8 11.1 5.4 12 4.1zM8.8 5a15 15 0 0 0-1.3 6H4.1A8 8 0 0 1 8.8 5zM4.1 13h3.4a15 15 0 0 0 1.3 6A8 8 0 0 1 4.1 13zm7.9 6.9c-.9-1.3-2-3.7-2.4-6.9h4.8c-.4 3.2-1.5 5.6-2.4 6.9zm3.2-.9a15 15 0 0 0 1.3-6h3.4a8 8 0 0 1-4.7 6z"/></svg>
      www.brightnookclean.example
    </li>
    <li>
      <svg viewBox="0 0 24 24" aria-hidden="true"><path d="M12 2a7 7 0 0 0-7 7c0 5.2 7 13 7 13s7-7.8 7-13a7 7 0 0 0-7-7zm0 9.5A2.5 2.5 0 1 1 12 6.5a2.5 2.5 0 0 1 0 5z"/></svg>
      Cedar Vale, NV 80999
    </li>
  </ul>

  <p class="credential">Bonded &amp; Insured</p>

  <div class="slogan-band">
    <p class="slogan">Helping your home shine for a cleaner tomorrow</p>
  </div>
</section>

</body>
</html>
```